サイト構成・基本的な要件については
https://zuvela.com/boards/7kQwLmTn28XpaRzd
をご参照ください。
ただ、レイアウトについては、各コンテンツへの導線が確保されていれば、
上記レイアウト案を必ず守る必要はございません。

写真素材については、
http://hakoyuki.jp/fetch/8b1d2f7a4c6e90135d7a8b2c4e6f1a3b5d7c9e0a
よりダウンロードください。
また、こちらだけですと作成が難しいと思いますので。。
http://gorumo.jp/
などから、10000円程度までならこちらにて購入可能です。

ロゴについては、
添付のデータを展開していただく形でご利用ください。

丸太のマークをご利用いただければ、
その他の要素(Wood Working Shop / 浅沼工房の丸太文字)については
必ずしも使用しなくてかまいません。
位置の変更も問題ございません。

【参考サイト】
http://www.surinavel.com/
http://kabuteya.jp/

白ベースの配色で、
少し木の温かみを感じるようなデザインを希望いたします。

基本レイアウト
については、必ずしも忠実である必要はありません。
特に今後大きく構成が変わる予定はございませんので、
各コンテンツへの導線を確保してあれば
必ずしも上記に準じている必要はありません。
ご自由にご提案いただいても結構です。
2カラムのご提案でも問題ございません。
また、当方jqueryを使用したコーディングも可能です。

恐れ入りますが、何卒よろしくお願いいたします。
http://www.lumio-t.hinoka.ne.jp/
茶系
【素材データについて】
よりダウンロードください。
http://gorumo.jp/
カンプデータにて作成頂き、納品時に当方にて購入したデータに差し替えていただければと存じます。

【参考サイト】
http://www.surinavel.com/
http://kabuteya.jp/

落ち着きがあり、信頼性を感じるデザインを希望いたします。
トップページで、いくつかの施工写真を見せられればと思います。
あまり無機質になりすぎず、木の温かみを感じるようなイメージですと
大変ありがたく存じます。

http://pagebase-lab.com/2012/166.html
http://pagebase-lab.com/2011/115.html
→フッター部分の参考です

ご提案に関しまして、不明点等ございましたらお気軽にお申し付けください。

クライアントとの協議の結果、こちらの案を採用させていただきました。
サイト全体の見やすさ、信頼感、清潔感
文字などの読みやすさが大変気に入り、
そちらが採用の決め手となりました。

この度は多数ご提案いただきありがとうございました。
当選に至らなかったランサー様におかれましては大変心苦しいのですが、
次の機会にぜひご提案いただければ幸甚です。
引き続き何卒よろしくお願いいたします。

```html
<!DOCTYPE html>
<html lang="ja">
<head>
<meta charset="utf-8">
<title>株式会社 浅沼工房</title>
<link href="https://fonts.googleapis.com/css2?family=Noto+Serif+JP:wght@400;600&family=Noto+Sans+JP:wght@400;500&display=swap" rel="stylesheet">
<style>
:root{
  --ink:#3a3632;
  --muted:#8a847c;
  --line:#e2ddd6;
  --beige:#f1eee9;
  --gray-band:#eeece8;
  --dark:#3b3a38;
  --green:#8fa451;
  --tag:#6f5a40;
  --white:#fff;
}
*{box-sizing:border-box;margin:0;padding:0}
html,body{width:1200px;height:2352px;overflow:hidden}
body{background:var(--white);color:var(--ink);font-family:"Noto Sans JP",sans-serif;font-size:14px;position:relative}
.serif{font-family:"Noto Serif JP",serif}
a{color:inherit;text-decoration:none}

/* header */
.site-header{height:72px;width:896px;margin:0 auto;display:flex;align-items:center;justify-content:space-between}
.brand{display:flex;align-items:center;gap:10px;font-family:"Noto Serif JP",serif;font-size:22px;font-weight:600;color:var(--ink)}
.brand-dot{width:26px;height:26px;border-radius:50%;background:var(--ink)}
.header-contact{display:flex;align-items:center;gap:18px}
.header-tel{text-align:right;font-family:"Noto Serif JP",serif}
.header-tel small{display:block;font-size:10px;color:var(--muted)}
.header-tel strong{font-size:20px;font-weight:400}
.btn-dark{background:var(--dark);color:#fff;font-size:13px;padding:10px 22px;border-radius:3px;display:flex;align-items:center;gap:8px}
.global-nav{border-top:1px solid var(--line);border-bottom:1px solid var(--line);height:48px}
.global-nav ul{list-style:none;width:896px;margin:0 auto;display:flex;height:100%}
.global-nav li{flex:1;display:flex;align-items:center;justify-content:center;font-family:"Noto Serif JP",serif;font-size:14px;border-left:1px solid var(--line)}
.global-nav li:last-child{border-right:1px solid var(--line)}
.global-nav li.current{color:var(--ink);font-weight:600}

/* hero */
.hero{background:var(--beige);padding:32px 0 40px}
.hero-visual{width:896px;height:448px;margin:0 auto;position:relative;background:linear-gradient(100deg,#9a8a74 0%,#b8a88e 40%,#d8d2c2 70%,#e9e7df 100%)}
.hero-copy{position:absolute;left:300px;top:40px;writing-mode:vertical-rl;color:#fff;font-family:"Noto Serif JP",serif;display:flex;gap:14px}
.hero-copy h1{font-size:56px;font-weight:600;letter-spacing:8px}
.hero-copy p{font-size:22px;letter-spacing:4px;padding-top:60px}

/* news + side */
.main-wrap{width:896px;margin:60px auto 0;display:flex;justify-content:space-between}
.news{width:608px}
.section-title{font-family:"Noto Serif JP",serif;font-size:22px;letter-spacing:4px;display:flex;align-items:baseline;gap:14px;padding-bottom:18px;border-bottom:2px solid var(--ink)}
.section-title span{font-size:12px;color:var(--muted);letter-spacing:2px}
.news-list{list-style:none}
.news-list li{height:64px;border-bottom:1px solid var(--line);display:flex;align-items:center;gap:24px;font-size:13px}
.news-list time{color:var(--muted);width:90px}
.news-list .tag{font-size:11px;border:1px solid var(--line);padding:2px 8px;color:var(--muted)}
.btn-more{display:inline-flex;align-items:center;gap:10px;border:1px solid var(--line);background:var(--beige);font-size:13px;padding:10px 26px}
.news .more-wrap{text-align:right;margin-top:36px}
.side{width:248px}
.contact-box{border:1px solid var(--line)}
.contact-box h3{background:var(--dark);color:#fff;font-size:13px;font-weight:400;text-align:center;padding:8px 0}
.contact-body{padding:16px 18px;font-size:12px;line-height:1.9}
.contact-body .name{font-family:"Noto Serif JP",serif;font-size:14px}
.contact-body .btn-dark{justify-content:center;margin-top:10px;font-size:12px;padding:8px}
.side-link{margin-top:20px;border:1px solid var(--line);height:62px;display:flex;align-items:center;gap:14px;padding:0 20px;font-family:"Noto Serif JP",serif;font-size:14px}
.side-link + .side-link{margin-top:14px}

/* works */
.works{background:var(--gray-band);margin-top:76px;padding:48px 0 60px}
.works-head{text-align:center;font-family:"Noto Serif JP",serif;font-size:24px;letter-spacing:6px}
.works-head span{font-size:12px;color:var(--muted);letter-spacing:2px;margin-left:10px}
.works-head svg{display:block;margin:0 auto 6px}
.works-grid{width:896px;margin:36px auto 0;display:flex;justify-content:space-between}
.work-card{width:280px}
.work-cap{display:flex;align-items:center;gap:10px;font-size:13px;margin-bottom:8px}
.work-cap .tag{background:var(--tag);color:#fff;font-size:11px;padding:3px 10px}
.work-photo{height:220px}
.work-card .btn-more{margin-top:16px;background:#fff;width:100%;justify-content:center}
.works .center{text-align:center;margin-top:40px}
.works .center .btn-more{background:#fff}

/* guide */
.guide{width:896px;margin:24px auto 0;display:flex;border-left:1px solid var(--line)}
.guide a{flex:1;height:120px;border-right:1px solid var(--line);display:flex;flex-direction:column;align-items:center;justify-content:center;gap:12px;font-family:"Noto Serif JP",serif;font-size:14px}

/* footer */
.site-footer{position:absolute;left:0;top:2000px;width:1200px;height:352px;background:var(--dark);color:#ddd}
.to-top{position:absolute;left:584px;top:-16px;width:32px;height:32px;border-radius:50%;background:var(--green);display:flex;align-items:center;justify-content:center}
.footer-inner{width:896px;margin:0 auto;padding-top:64px;display:flex;font-size:12px;line-height:2}
.footer-company{width:383px}
.footer-company .name{font-family:"Noto Serif JP",serif;font-size:15px;color:#fff}
.footer-company .btn-dark{display:inline-flex;background:#fff;color:var(--ink);margin-top:8px;font-size:12px;padding:6px 16px}
.footer-col{width:180px;list-style:none}
.footer-col li::before{content:"・";color:var(--green)}
.footer-col .sub{padding-left:14px}
.footer-col .sub::before{content:"- ";color:#999}
.copyright{position:absolute;bottom:14px;width:100%;text-align:center;font-size:10px;color:#999}
</style>
</head>
<body>

<header class="site-header">
  <a class="brand" href="#"><span class="brand-dot"></span>株式会社 浅沼工房</a>
  <div class="header-contact">
    <div class="header-tel"><small>受付時間 平日8:00〜17:00</small><strong>Tel. 0463-71-4580</strong></div>
    <a class="btn-dark" href="#">
      <svg width="14" height="10" viewBox="0 0 14 10"><rect x=".5" y=".5" width="13" height="9" fill="none" stroke="#fff"/><path d="M.5 .5 7 6 13.5 .5" fill="none" stroke="#fff"/></svg>お問い合わせ</a>
  </div>
</header>
<nav class="global-nav">
  <ul>
    <li class="current">HOME</li><li>営業品目</li><li>施工例</li><li>お役立ち情報</li><li>よくあるご質問</li><li>会社概要</li>
  </ul>
</nav>

<section class="hero">
  <div class="hero-visual" role="img" aria-label="木の幹に大人と子どもの手が添えられた写真">
    <div class="hero-copy">
      <h1>創業六十二年</h1>
      <p>木の温もりを届けます</p>
    </div>
  </div>
</section>

<div class="main-wrap">
  <section class="news">
    <h2 class="section-title">新着情報<span>News</span></h2>
    <ul class="news-list">
      <li><time>2017.04.30</time><span class="tag">お知らせ</span>ホームページをリニューアルしました。</li>
      <li><time>2017.04.30</time><span class="tag">お知らせ</span>ゴールデンウィーク休業のお知らせです。</li>
      <li><time>2017.04.30</time><span class="tag">施工例</span>施工例に住宅の実例を追加しました。</li>
      <li><time>2017.04.30</time><span class="tag">お知らせ</span>見学会の日程を更新いたしました。</li>
      <li><time>2017.04.30</time><span class="tag">お知らせ</span>お役立ち情報を更新いたしました。</li>
    </ul>
    <div class="more-wrap"><a class="btn-more" href="#"><svg width="8" height="10"><path d="M1 1l5 4-5 4" fill="none" stroke="#3a3632"/></svg>新着情報一覧を見る</a></div>
  </section>

  <aside class="side">
    <div class="contact-box">
      <h3>お気軽にご相談ください</h3>
      <div class="contact-body">
        <div class="name">株式会社 浅沼工房</div>
        TEL 0463-71-4580<br>
        FAX 0463-71-4581<br>
        受付時間 8:00〜17:00
        <a class="btn-dark" href="#">お問い合わせフォーム</a>
      </div>
    </div>
    <a class="side-link" href="#"><svg width="22" height="22" viewBox="0 0 22 22"><rect x="3" y="4" width="16" height="15" fill="none" stroke="#3a3632"/><path d="M6 9h10M6 13h10" stroke="#3a3632"/></svg>会社概要</a>
    <a class="side-link" href="#"><svg width="22" height="22" viewBox="0 0 22 22"><path d="M11 20s-6-6.5-6-11a6 6 0 0112 0c0 4.5-6 11-6 11z" fill="none" stroke="#3a3632"/><circle cx="11" cy="9" r="2" fill="#3a3632"/></svg>アクセスマップ</a>
  </aside>
</div>

<section class="works">
  <h2 class="works-head"><svg width="22" height="16" viewBox="0 0 22 16"><path d="M2 14C4 5 10 2 20 2 18 11 12 14 2 14z" fill="#8fa451"/></svg>施工例<span>Works</span></h2>
  <div class="works-grid">
    <article class="work-card">
      <div class="work-cap"><span class="tag">住宅</span>A様邸</div>
      <div class="work-photo" role="img" aria-label="白い壁と木の床の住宅内観写真" style="background:linear-gradient(160deg,#f2efea,#cdbfa8)"></div>
      <a class="btn-more" href="#">詳細を見る</a>
    </article>
    <article class="work-card">
      <div class="work-cap"><span class="tag">店舗</span>某飲食店様</div>
      <div class="work-photo" role="img" aria-label="木製建具の店舗内観写真" style="background:linear-gradient(160deg,#c9a57a,#8c6a45)"></div>
      <a class="btn-more" href="#">詳細を見る</a>
    </article>
    <article class="work-card">
      <div class="work-cap"><span class="tag">医療</span>B病院様</div>
      <div class="work-photo" role="img" aria-label="木の手すりがある明るい施設内観写真" style="background:linear-gradient(160deg,#f4efe6,#d6c1a0)"></div>
      <a class="btn-more" href="#">詳細を見る</a>
    </article>
  </div>
  <div class="center"><a class="btn-more" href="#"><svg width="8" height="10"><path d="M1 1l5 4-5 4" fill="none" stroke="#3a3632"/></svg>施工例一覧を見る</a></div>
</section>

<nav class="guide">
  <a href="#"><svg width="30" height="30" viewBox="0 0 30 30"><rect x="5" y="4" width="20" height="22" fill="none" stroke="#3a3632"/><path d="M9 10h12M9 15h12M9 20h8" stroke="#3a3632"/></svg>営業品目</a>
  <a href="#"><svg width="30" height="30" viewBox="0 0 30 30"><circle cx="15" cy="13" r="8" fill="none" stroke="#3a3632"/><path d="M12 23h6M13 26h4" stroke="#3a3632"/></svg>お役立ち情報</a>
  <a href="#"><svg width="30" height="30" viewBox="0 0 30 30"><circle cx="15" cy="15" r="11" fill="none" stroke="#3a3632"/><path d="M12 12a3 3 0 116 0c0 2-3 2-3 5" fill="none" stroke="#3a3632"/><circle cx="15" cy="21" r="1" fill="#3a3632"/></svg>よくあるご質問</a>
</nav>

<footer class="site-footer">
  <a class="to-top" href="#"><svg width="12" height="8"><path d="M1 7l5-5 5 5" fill="none" stroke="#fff" stroke-width="2"/></svg></a>
  <div class="footer-inner">
    <div class="footer-company">
      <div class="name">株式会社 浅沼工房</div>
      TEL 0463-71-4580<br>
      FAX 0463-71-4581<br>
      受付時間 8:00〜17:00（平日）<br>
      <a class="btn-dark" href="#">お問い合わせフォーム</a>
    </div>
    <ul class="footer-col">
      <li>営業品目</li><li>お役立ち情報</li>
    </ul>
    <ul class="footer-col">
      <li>施工例</li>
      <li class="sub">住宅</li><li class="sub">店舗</li><li class="sub">医療</li><li class="sub">グループホーム</li><li class="sub">その他</li>
    </ul>
    <ul class="footer-col">
      <li>よくあるご質問</li><li>会社概要</li>
    </ul>
  </div>
  <p class="copyright">Copyright © 浅沼工房 All Rights Reserved.</p>
</footer>

</body>
</html>
```